Business card design needed

Our company background is that we provides transfers to and from the airport, social & corporate events, weddings.
We are also available for charter for birthday party, wine tastings, concerts, anniversary, school balls etc.
Our business cards have to reflect that we have a professional company, they are our first contact and have to stand out from the other 'players' in the market.

Industry/Entity Type

School

Contact Information for Business Card

VESTAR PTH, Teodor & Marguerite, mob: 0427 381 592, PO Box 284, Kwinana WA 6966, ABN 52 614 203 178, Lic 7169/2058,

Requirements
Must have
• Telephone number: 0427 381 592
Website: www.VESTARPTH.com.au
postal address: PO Box 284, Kwinana WA 6966
Licences: Lic 7169/2058

***If using the new photo (one with the bus and buildings behind it), if possible can the buildings be cropped out. Thanks
Nice to have
• would be nice to have the pics of the vehicle(s), preferred the Vel on the card but not too fussed.
Should not have
• Picture of vehicle we don't have in our fleet. (We ONLY have the Velarions and Murako Densa mini bus)

```html
<!DOCTYPE html>
<html lang="en">
<head>
<meta charset="utf-8">
<title>Vestar PTH Business Card</title>
<link rel="stylesheet" href="https://fonts.googleapis.com/css2?family=Marcellus&family=Pinyon+Script&family=Ubuntu:wght@400;500&display=swap">
<style>
  :root {
    --stage: #2a2a2a;
    --card: #0c0c0c;
    --card-edge: #1c1c1c;
    --photo-light: #3a3a3a;
    --photo-dark: #080808;
    --ink: #f2f2f2;
    --ink-soft: #d8d8d8;
  }
  * { margin: 0; padding: 0; box-sizing: border-box; }
  html, body {
    width: 1200px;
    height: 861px;
    overflow: hidden;
    background: var(--stage);
  }
  .stage {
    position: relative;
    width: 1200px;
    height: 861px;
    display: flex;
    align-items: center;
    justify-content: center;
  }
  .card {
    position: relative;
    width: 880px;
    height: 555px;
    border-radius: 26px;
    overflow: hidden;
    background: var(--card);
    border: 1px solid var(--card-edge);
    box-shadow: 0 18px 50px rgba(0,0,0,0.5);
    color: var(--ink);
  }
  .card__photo {
    position: absolute;
    inset: 0;
    background:
      radial-gradient(ellipse 62% 55% at 50% 42%, var(--photo-light) 0%, #1d1d1d 55%, var(--photo-dark) 100%);
  }
  .card__content {
    position: relative;
    height: 100%;
    display: flex;
    flex-direction: column;
    align-items: center;
  }
  .brand {
    margin-top: 58px;
    text-align: center;
  }
  .brand__name {
    font-family: "Marcellus", serif;
    font-size: 78px;
    line-height: 1;
    letter-spacing: 4px;
    color: var(--ink-soft);
  }
  .brand__tagline {
    margin-top: 10px;
    margin-left: 150px;
    font-family: "Marcellus", serif;
    font-size: 24px;
    color: var(--ink-soft);
  }
  .owners {
    margin-top: 34px;
    font-family: "Pinyon Script", cursive;
    font-size: 76px;
    line-height: 1;
    color: var(--ink);
  }
  .details {
    margin-top: 44px;
    width: 720px;
    display: grid;
    grid-template-columns: 1fr auto;
    column-gap: 30px;
    row-gap: 18px;
    font-family: "Ubuntu", sans-serif;
    font-size: 21px;
    color: var(--ink);
  }
  .details__label { font-weight: 500; }
  .details__item { font-weight: 400; }
  .details__item--right { font-size: 18px; }
  .website {
    margin-top: 34px;
    font-family: "Ubuntu", sans-serif;
    font-weight: 500;
    font-size: 25px;
    color: var(--ink);
  }
</style>
</head>
<body>
  <main class="stage">
    <section class="card">
      <div class="card__photo" role="img" aria-label="Photograph of a dark luxury Velarion sedan seen from the front, over a fine mesh texture"></div>
      <div class="card__content">
        <header class="brand">
          <div class="brand__name">Vestar</div>
          <div class="brand__tagline">Luxury Car &amp; Coach</div>
        </header>
        <h1 class="owners">Teodor &amp; Marguerite</h1>
        <div class="details">
          <p class="details__item"><span class="details__label">Address:</span> PO Box 284, Kwinana WA 6966</p>
          <p class="details__item details__item--right"><span class="details__label">Licences:</span> Lic 7169/2058</p>
          <p class="details__item"><span class="details__label">Telephone:</span> 0427 381 592</p>
          <p class="details__item details__item--right"><span class="details__label">ABN:</span> 52 614 203 178</p>
        </div>
        <p class="website">www.VESTARPTH.com.au</p>
      </div>
    </section>
  </main>
</body>
</html>
```